Harbor Business Cards

I need a business card designed with the following information.

Company Name: Harbor Wealth Management
Name: BriAnne Dockery
Title: Executive Assistant
Cell: (555) 201-0173
Direct Line: (555) 306-0148
Email: brianne@harborwmx.com
Address: 20537 W. Marlowe PKWY Ste. B
Cedarbrook, TX 77390

I have attached the logo.
I would like it in navy blue and silver.
Thanks.

```html
<!DOCTYPE html>
<html lang="en">
<head>
<meta charset="utf-8">
<title>Harbor Wealth Management – Business Card</title>
<link href="https://fonts.googleapis.com/css2?family=Open+Sans:wght@400;600&display=swap" rel="stylesheet">
<style>
  :root {
    --navy: #0e2240;
    --silver: #a3a4a6;
    --white: #ffffff;
    --ink: #1a1a1a;
    --backdrop: #d2d4d6;
  }
  * { margin: 0; padding: 0; box-sizing: border-box; }
  html, body { width: 1200px; height: 1106px; overflow: hidden; }
  body {
    background: var(--backdrop);
    font-family: "Open Sans", Arial, sans-serif;
    position: relative;
  }
  .card {
    position: absolute;
    width: 760px;
    height: 420px;
    border-radius: 34px;
    overflow: hidden;
  }
  .card-front { left: 80px; top: 70px; background: var(--white); border: 1px solid #9a9a9a; }
  .card-back { left: 360px; top: 600px; background: var(--navy); }
  .front-band { position: absolute; inset: 0; width: 100%; height: 100%; }
  .holder { position: absolute; right: 44px; top: 26px; text-align: right; color: var(--white); }
  .holder-name { font-size: 27px; font-weight: 400; line-height: 1.2; }
  .holder-title { font-size: 20px; font-weight: 400; }
  .brand {
    position: absolute; left: 70px; top: 300px;
    display: flex; align-items: center; gap: 12px;
  }
  .brand-mark { width: 22px; height: 22px; border-radius: 50%; background: var(--navy); flex: none; }
  .brand-name { color: var(--navy); font-size: 26px; font-weight: 400; letter-spacing: 1px; }
  .address {
    position: absolute; left: 78px; bottom: 30px;
    color: var(--ink); font-size: 19px; line-height: 1.5; font-style: normal;
  }
  .contacts {
    position: absolute; right: 40px; bottom: 22px;
    list-style: none; color: var(--ink); font-size: 19px;
  }
  .contacts li { display: flex; align-items: center; justify-content: flex-end; gap: 8px; line-height: 1.95; }
  .contacts svg { width: 19px; height: 19px; flex: none; }
  .back-brand {
    position: absolute; left: 0; right: 0; top: 145px;
    display: flex; align-items: center; justify-content: center; gap: 18px;
  }
  .back-brand .brand-mark { width: 34px; height: 34px; background: var(--white); }
  .back-brand .brand-name { color: var(--white); font-size: 40px; }
  .website {
    position: absolute; left: 0; right: 0; bottom: 60px; text-align: center;
    color: var(--white); font-size: 24px; letter-spacing: 3px;
  }
</style>
</head>
<body>
  <section class="card card-front">
    <svg class="front-band" viewBox="0 0 760 420" preserveAspectRatio="none" aria-hidden="true">
      <path d="M0 0 H760 V172 C560 90 330 95 0 92 Z" fill="var(--navy)"/>
      <path d="M0 118 C280 86 560 108 760 202 V220 C560 128 280 104 0 132 Z" fill="var(--silver)"/>
    </svg>
    <div class="holder">
      <div class="holder-name">BriAnne Dockery</div>
      <div class="holder-title">Executive Assistant</div>
    </div>
    <div class="brand">
      <span class="brand-mark"></span>
      <span class="brand-name">Harbor Wealth Management</span>
    </div>
    <ul class="contacts">
      <li>
        <svg viewBox="0 0 20 20" aria-hidden="true"><circle cx="10" cy="10" r="8.5" fill="none" stroke="var(--ink)" stroke-width="1.6"/><path d="M7 5.5 L8.6 7.6 L7.8 8.8 C8.5 10.3 9.7 11.5 11.2 12.2 L12.4 11.4 L14.5 13 L13.3 14.5 C9.5 14 6 10.5 5.5 6.7 Z" fill="var(--ink)"/></svg>
        (555) 201-0173
      </li>
      <li>
        <svg viewBox="0 0 20 20" aria-hidden="true"><circle cx="10" cy="10" r="8.5" fill="none" stroke="var(--ink)" stroke-width="1.6"/><path d="M7 5.5 L8.6 7.6 L7.8 8.8 C8.5 10.3 9.7 11.5 11.2 12.2 L12.4 11.4 L14.5 13 L13.3 14.5 C9.5 14 6 10.5 5.5 6.7 Z" fill="var(--ink)"/></svg>
        (555) 306-0148(Direct Line)
      </li>
      <li>
        <svg viewBox="0 0 20 20" aria-hidden="true"><circle cx="10" cy="10" r="8.5" fill="none" stroke="var(--ink)" stroke-width="1.6"/><rect x="5.5" y="7" width="9" height="6.5" fill="none" stroke="var(--ink)" stroke-width="1.3"/><path d="M5.5 7 L10 10.5 L14.5 7" fill="none" stroke="var(--ink)" stroke-width="1.3"/></svg>
        brianne@harborwmx.com
      </li>
    </ul>
    <address class="address">
      20537 W. Marlowe PKWY Ste. B<br>
      Cedarbrook, TX 77390
    </address>
  </section>

  <section class="card card-back">
    <div class="back-brand">
      <span class="brand-mark"></span>
      <span class="brand-name">Harbor Wealth Management</span>
    </div>
    <div class="website">www.harborwmx.com</div>
  </section>
</body>
</html>
```